TEK Logistics - Banner 2.5' x 8' for 20+ locations

Need a banner designed that will pop. This banner will be displayed at over 20 of our transportation facilities. Goal is for the banner to grab the attention of employees, contractors and clients and help reinforce our mission and core values. Designed needs to include TEK Logo, our core values and mission statement. Red and Black are the main company colors and we need to stay within that theme and color pallet. Attached is a previous version that was too basic and boring. Willing to consider a design that excludes the mission statement.

Gathering more feedback

```html
<!DOCTYPE html>
<html lang="en">
<head>
<meta charset="UTF-8">
<title>TEK Logistics – Core Values Banner</title>
<link href="https://fonts.googleapis.com/css2?family=Open+Sans:wght@600;700&family=PT+Sans+Narrow&display=swap" rel="stylesheet">
<style>
  :root {
    --backdrop: #c6bfbc;
    --brand-red: #c41e17;
    --brand-black: #1f1d1d;
    --panel-white: #ece9e8;
    --text-light: #f2efee;
    --text-muted: #dcd8d7;
    --logo-ink: #2a2626;
  }
  html, body {
    margin: 0;
    padding: 0;
    width: 1200px;
    height: 1000px;
    overflow: hidden;
    background: var(--backdrop);
  }
  .canvas {
    position: relative;
    width: 1200px;
    height: 1000px;
  }
  .banner {
    position: absolute;
    left: 0;
    top: 0;
    width: 1200px;
    height: 1000px;
  }
  .banner__values text {
    font-family: "Open Sans", Arial, sans-serif;
    font-weight: 600;
    fill: var(--text-light);
  }
  .banner__mission text {
    font-family: "PT Sans Narrow", "Arial Narrow", sans-serif;
    font-size: 18px;
    fill: var(--text-muted);
  }
  .banner__brand text {
    font-family: "Open Sans", Arial, sans-serif;
    font-weight: 700;
    fill: var(--logo-ink);
  }
  .bracket {
    fill: none;
    stroke: var(--text-muted);
    stroke-width: 2.5;
  }
</style>
</head>
<body>
<main class="canvas">
  <svg class="banner" viewBox="0 0 1200 1000" xmlns="http://www.w3.org/2000/svg" aria-label="TEK Logistics core values banner">
    <rect class="banner__field" x="50" y="315" width="1100" height="345" fill="var(--brand-red)"/>
    <path class="banner__base-band" d="M50 553 Q500 578 978 568 L1050 660 L50 660 Z" fill="var(--brand-black)"/>
    <path class="banner__brand-panel" d="M1150 420 L978 568 L1050 660 L1150 660 Z" fill="var(--panel-white)"/>

    <g class="banner__values">
      <text x="402" y="383" font-size="19" textLength="418" lengthAdjust="spacingAndGlyphs">DO THE RIGHT THINGS FOR THE RIGHT REASONS</text>
      <text x="545" y="404" font-size="22" textLength="405" lengthAdjust="spacingAndGlyphs">PURSUE GROWTH AND DEVELOPMENT</text>
      <text x="283" y="434" font-size="28" textLength="485" lengthAdjust="spacingAndGlyphs">BUILD A POSITIVE TEAM ATMOSPHERE</text>
      <text x="452" y="467" font-size="32" textLength="488" lengthAdjust="spacingAndGlyphs">DELIVER WOW THROUGH SERVICE</text>
      <text x="410" y="503" font-size="37" textLength="415" lengthAdjust="spacingAndGlyphs">DO EVERYTHING SAFELY</text>
      <text x="535" y="543" font-size="42" textLength="197" lengthAdjust="spacingAndGlyphs">HAVE FUN</text>
    </g>

    <g class="banner__mission">
      <path class="bracket" d="M286 604 V588 H302"/>
      <text x="615" y="613" text-anchor="middle" textLength="616" lengthAdjust="spacingAndGlyphs">Provide the best customer experience while creating an environment of growth</text>
      <text x="615" y="638" text-anchor="middle" textLength="546" lengthAdjust="spacingAndGlyphs">and opportunity for our customers, employees, and service providers.</text>
      <path class="bracket" d="M924 642 H940 V626"/>
    </g>

    <g class="banner__brand">
      <text x="1075" y="584" font-size="30" text-anchor="middle">TEK</text>
      <text x="1075" y="602" font-size="12" text-anchor="middle" letter-spacing="2">LOGISTICS</text>
    </g>
  </svg>
</main>
</body>
</html>
```